Clean Plinth Ads Banner Design For A Finance Company

Hi,
We're a UK based finance company and are looking for new banner ads to use on the Plinth Display Network.
We want the end product to stand out by using strong, minimal design - ideally starting from a dark theme, although I'm open to ideas.
The copy should read:
'Fast Bridging Loans From 0.39% PM'
Once we have these designs agreed, we are looking to replicate them for other products, changing only the text on each ad - for example, 'commercial mortgage service you can rely on' or 'development finance service you can rely on'.
The colours used on our website are the following:
Black - #040303
Orange - #f79124
White - #ffffff
Grey - #ffffff
Example ads that I like - https://www.brimcastle.com/wp-content/uploads/2021/07/plinth-display-ads-example-2-final.png.webp
2 - https://quendrahub.com/wp-content/uploads/2020/03/fbdd56ba3bd16c7a8debb13a411de786.jpg

```html
<!DOCTYPE html>
<html lang="en">
<head>
<meta charset="utf-8">
<title>Arkwell Finance – Bridging Loan Display Banners</title>
<link rel="stylesheet" href="https://fonts.googleapis.com/css2?family=Fira+Sans:wght@400;600;700&family=Oswald:wght@500&family=Open+Sans:wght@400&display=swap">
<style>
  :root {
    --black: #040303;
    --orange: #f79124;
    --white: #ffffff;
    --ink: #1c1c1c;
    --board-dark: #252525;
    --board-mid: #3a3a3a;
    --photo-light: #f7f6f4;
    --photo-mid: #e2ddd6;
    --photo-warm: #d8cbbb;
    --badge-red: #c8161d;
  }
  * { box-sizing: border-box; margin: 0; padding: 0; }
  html, body { width: 1200px; height: 1200px; overflow: hidden; background: var(--board-dark); }
  .board { position: relative; width: 1200px; height: 1200px; overflow: hidden; font-family: "Fira Sans", sans-serif; color: var(--ink); }
  .board-photo { position: absolute; inset: 0; background: radial-gradient(ellipse at 72% 45%, var(--board-mid) 0%, #2b2b2b 45%, var(--board-dark) 100%); }
  .board-band { position: absolute; left: 0; top: 0; }
  .board-brand { position: absolute; left: 110px; top: 100px; font-weight: 700; font-size: 48px; color: #3b2410; letter-spacing: 1px; }

  .size-label { position: absolute; font-family: "Open Sans", sans-serif; font-size: 13px; color: var(--white); transform: translateX(-100%); }

  .banner { position: absolute; background: linear-gradient(#ffffff, #f4f4f4); overflow: hidden; box-shadow: 0 0 0 1px rgba(255,255,255,.15); }
  .banner-photo { position: absolute; left: 0; top: 0; background: linear-gradient(120deg, var(--photo-light) 0%, var(--photo-mid) 60%, var(--photo-warm) 100%); }
  .banner-slant { position: absolute; }
  .banner-brand { position: absolute; font-weight: 700; color: var(--orange); line-height: 1; }
  .badge { position: absolute; border-radius: 50%; background: var(--orange); box-shadow: 0 0 0 3px var(--badge-red); }
  .headline { position: absolute; font-weight: 700; color: var(--ink); white-space: nowrap; }
  .tagline { position: absolute; font-weight: 400; color: var(--ink); white-space: nowrap; }
  .tagline em, .headline em { font-style: normal; font-weight: 600; color: var(--orange); text-decoration: underline; text-underline-offset: 2px; }
  .benefits { position: absolute; list-style: none; }
  .benefits li { display: flex; align-items: center; white-space: nowrap; color: var(--ink); }
  .benefits svg { flex: none; }
  .benefits b { font-weight: 600; text-decoration: underline; margin-right: .25em; }
  .benefits .trail { font-weight: 600; text-decoration: underline; margin-left: .25em; }
  .cta { position: absolute; display: flex; align-items: center; justify-content: center; gap: 6px; background: var(--orange); color: var(--white); font-weight: 600; text-transform: uppercase; box-shadow: 0 0 0 3px rgba(247,145,36,.35); white-space: nowrap; }
  .phone { position: absolute; font-family: "Oswald", sans-serif; font-weight: 500; color: var(--ink); white-space: nowrap; }

  .key-points { position: absolute; left: 110px; top: 912px; font-family: "Open Sans", sans-serif; color: var(--white); }
  .key-points h2 { font-weight: 400; font-size: 23px; text-decoration: underline; text-underline-offset: 4px; margin-bottom: 26px; }
  .key-points li { list-style: none; font-size: 23px; line-height: 32px; }
</style>
</head>
<body>
<div class="board">
  <div class="board-photo" role="img" aria-label="Dimmed photo of a young family sitting on the floor under a cardboard roof shape"></div>
  <svg class="board-band" width="1200" height="1200" viewBox="0 0 1200 1200" aria-hidden="true">
    <polygon points="264,1200 1200,1088 1200,1200" fill="var(--orange)"/>
  </svg>
  <div class="board-brand">Arkwell Finance</div>

  <div class="size-label" style="left:349px; top:248px;">300 X 600</div>
  <div class="banner" style="left:109px; top:271px; width:240px; height:480px;">
    <div class="banner-photo" style="width:240px; height:225px;" role="img" aria-label="Photo of a smiling family sitting among moving boxes under a cardboard roof"></div>
    <svg class="banner-slant" style="left:0; top:190px;" width="240" height="50" viewBox="0 0 240 50" aria-hidden="true">
      <polygon points="0,45 240,6 240,30 0,50" fill="var(--orange)"/>
      <polygon points="0,46 240,30 240,50 0,50" fill="#ffffff"/>
    </svg>
    <div class="banner-brand" style="left:30px; top:22px; font-size:20px;">Arkwell Finance</div>
    <div class="badge" style="left:50px; top:186px; width:60px; height:60px;"></div>
    <div class="headline" style="left:14px; top:264px; font-size:22px;">Bridging Loan Service</div>
    <div class="tagline" style="left:14px; top:293px; font-size:17px;">You Can <em>Rely On</em></div>
    <ul class="benefits" style="left:27px; top:331px; font-size:12.5px; line-height:19px;">
      <li><svg width="20" height="10" viewBox="0 0 20 10"><path d="M1 1l4 4-4 4M6 1l4 4-4 4" fill="none" stroke="var(--orange)" stroke-width="1.6"/></svg><b>5 Star</b> Rated Service</li>
      <li><svg width="20" height="10" viewBox="0 0 20 10"><path d="M1 1l4 4-4 4M6 1l4 4-4 4" fill="none" stroke="var(--orange)" stroke-width="1.6"/></svg>No Broker<span class="trail">Fees</span></li>
    </ul>
    <div class="cta" style="left:29px; top:389px; width:182px; height:41px; font-size:14px;">Talk to an expert
      <svg width="12" height="10" viewBox="0 0 12 10"><path d="M1 1l4 4-4 4M6 1l4 4-4 4" fill="none" stroke="#fff" stroke-width="1.8"/></svg></div>
    <div class="phone" style="left:40px; top:436px; font-size:21px;">CALL: 01632 960418</div>
    <svg class="banner-slant" style="left:0; top:460px;" width="240" height="20" viewBox="0 0 240 20" aria-hidden="true">
      <polygon points="130,20 240,6 240,20" fill="var(--orange)"/>
    </svg>
  </div>

  <div class="size-label" style="left:658px; top:503px;">336 X 280</div>
  <div class="banner" style="left:389px; top:527px; width:269px; height:224px;">
    <div class="banner-photo" style="width:269px; height:118px;" role="img" aria-label="Photo of a smiling family sitting among moving boxes under a cardboard roof"></div>
    <svg class="banner-slant" style="left:0; top:92px;" width="269" height="40" viewBox="0 0 269 40" aria-hidden="true">
      <polygon points="140,30 269,4 269,24 200,40" fill="var(--orange)"/>
      <polygon points="0,40 269,24 269,40" fill="#ffffff"/>
    </svg>
    <div class="banner-brand" style="left:26px; top:18px; font-size:17px;">Arkwell Finance</div>
    <div class="badge" style="left:40px; top:72px; width:50px; height:50px;"></div>
    <div class="headline" style="left:16px; top:140px; font-size:14.5px;">Bridging Loan Service <span style="font-weight:400; font-size:12px;">You Can <em>Rely On</em></span></div>
    <ul class="benefits" style="left:24px; top:165px; font-size:10px; line-height:14px; display:flex; gap:14px;">
      <li><svg width="16" height="8" viewBox="0 0 20 10"><path d="M1 1l4 4-4 4M6 1l4 4-4 4" fill="none" stroke="var(--orange)" stroke-width="1.8"/></svg><b>5 Star</b> Rated Service</li>
      <li><svg width="16" height="8" viewBox="0 0 20 10"><path d="M1 1l4 4-4 4M6 1l4 4-4 4" fill="none" stroke="var(--orange)" stroke-width="1.8"/></svg>No Broker<span class="trail">Fees</span></li>
    </ul>
    <div class="cta" style="left:20px; top:192px; width:112px; height:22px; font-size:9.5px;">Talk to an expert
      <svg width="9" height="7" viewBox="0 0 12 10"><path d="M1 1l4 4-4 4M6 1l4 4-4 4" fill="none" stroke="#fff" stroke-width="2"/></svg></div>
    <div class="phone" style="left:145px; top:192px; font-size:14px;">CALL: 01632 960418</div>
    <svg class="banner-slant" style="left:0; top:210px;" width="269" height="14" viewBox="0 0 269 14" aria-hidden="true">
      <polygon points="180,14 269,4 269,14" fill="var(--orange)"/>
    </svg>
  </div>

  <div class="size-label" style="left:689px; top:763px;">728 X 90</div>
  <div class="banner" style="left:109px; top:783px; width:582px; height:72px;">
    <div class="banner-photo" style="width:190px; height:72px;" role="img" aria-label="Photo of a smiling family sitting among moving boxes under a cardboard roof"></div>
    <svg class="banner-slant" style="left:170px; top:0;" width="30" height="72" viewBox="0 0 30 72" aria-hidden="true">
      <polygon points="8,0 16,0 28,72 20,72" fill="var(--orange)"/>
      <polygon points="16,0 30,0 30,72 28,72" fill="#ffffff"/>
    </svg>
    <div class="banner-brand" style="left:10px; top:12px; font-size:13px;">Arkwell Finance</div>
    <div class="headline" style="left:203px; top:4px; font-size:13px;">Bridging Loan Service</div>
    <div class="tagline" style="left:203px; top:21px; font-size:10.5px;">You Can <em>Rely On</em></div>
    <ul class="benefits" style="left:207px; top:40px; font-size:9.5px; line-height:14px;">
      <li><svg width="16" height="8" viewBox="0 0 20 10"><path d="M1 1l4 4-4 4M6 1l4 4-4 4" fill="none" stroke="var(--orange)" stroke-width="1.8"/></svg><b>5 Star</b> Rated Service</li>
      <li><svg width="16" height="8" viewBox="0 0 20 10"><path d="M1 1l4 4-4 4M6 1l4 4-4 4" fill="none" stroke="var(--orange)" stroke-width="1.8"/></svg>No Broker<span class="trail">Fees</span></li>
    </ul>
    <div class="cta" style="left:353px; top:15px; width:115px; height:22px; font-size:9.5px;">Talk to an expert
      <svg width="9" height="7" viewBox="0 0 12 10"><path d="M1 1l4 4-4 4M6 1l4 4-4 4" fill="none" stroke="#fff" stroke-width="2"/></svg></div>
    <div class="phone" style="left:357px; top:44px; font-size:14px;">CALL: 01632 960418</div>
    <svg class="banner-slant" style="left:560px; top:0;" width="22" height="72" viewBox="0 0 22 72" aria-hidden="true">
      <polygon points="0,0 22,0 22,40" fill="var(--orange)"/>
    </svg>
    <div class="badge" style="left:510px; top:12px; width:46px; height:46px;"></div>
  </div>

  <section class="key-points">
    <h2>Key Points</h2>
    <ul>
      <li>Adobe PhotoShop Design</li>
      <li>Easy Editable</li>
      <li>Use Free Fonts</li>
      <li>Clean Design</li>
    </ul>
  </section>
</div>
</body>
</html>
```